The Busy Wren Organic & Natural Soaps is looking for label designs (along with the business card proje

This is my scope and requirements:
Labelling project:
This is related to the Label project I also opened up. (The Busy Wren Organic & Natural Soaps needs a good business card (Contest) )
I have attached an initial draft at a logo I tried to come up with for a business card and labelling/marketing. I am hoping that you can take this logo and 'run with it' to finesse it, make it look unique and professional. If you need to change it, I am open to ideas.
I find that labelling/packaging is hard for me to make it look 'professional' so I am coming to the experts!
I am looking for label designs for 2 different bottles and 2 different bar soaps:
1) Organic Bar Soap (2 possibilities: 1) Kraft 'cigar' band around soap with twine, 2) Kraft soap box with Kraft sticker Labels
2) Natural Olive Oil Based Bar Soap (labelling can be same as Organic but with distinct info)
3) Organic Hand Washes (clear square bottles, 250ml with natural pump)
4) Natural Olive Oil Based Body Wash (taper bottle 200ml with metal silver disc top caps)
I am a start up at home company making Organic and Natural Bar soaps, hand soaps, body washes.
All of my ingredients are organic or natural and will include natural essential oils, exfoliants, natural powders/colours, etc.
Some of the names are: Brisquel (feisty, energetic soap), Dunmoor (more of a sandalwood earthy tones with a sandalwood powder exfoliant), Frosk (maybe changing this name - fresh scented), Plum Cardamom (lemongrass/ginger, exfoliants), etc....
If you need more information, please let me know!
Please find attached: Kraft Paper I am looking at to possibly wrap the Bar Soaps in (I like the different colour concept and am trying to decide between diff colours of Wendell Prask paper to wrap around or plain kraft paper.. whichever the new logo concept will look best with.
The bottles I will be using for the hand soap (250ml square) and the body wash (200ml tapered)
OLD POST:
Hello! I am a start up business that is specializing in making luxury organic bar soaps, natural olive oil bar soaps, organic hand wash, natural olive oil body wash/shower gel that will include essential oils, exfoliants, natural powders, etc. (also accessories: wood soap dishes, etc) .. I am looking for a great designer that can provide me with the business card and labelling designs! I appreciate feedback, ideas on how I can receive a great design to help sell my products!
I am attaching my initial logo design that I would like to keep - but am looking for someone to 'finesse' it or make it more professional/unique looking.
Again, this is hand in hand with the business card project I submitted.
Thanks!
Mirela
Updates
I am sorry for the lack of direction or Scope of the project. I am new at this board.
Labelling project:
I have attached an initial draft at a logo I tried to come up with for a business card and labelling/marketing. I am hoping that you can take this logo and 'run with it' to finesse it, make it look unique and professional.
If you need more information, please let me know.
Hello; I just wanted to let everyone know that if you feel that this brand needs a different logo, I am open to ideas (if you don't think the one I started with is ok). I am coming to the experts here!
Just to confirm also - this is related to the business card project, therefore, there are 2 projects, 2 payments! :)
Cheers

```html
<!DOCTYPE html>
<html lang="en">
<head>
<meta charset="utf-8">
<title>The Busy Wren – Organic Hand Wash Label, Dunmoor</title>
<link rel="stylesheet" href="https://fonts.googleapis.com/css2?family=Sorts+Mill+Goudy&family=Lobster+Two:ital,wght@1,700&family=Libre+Baskerville:wght@700&display=swap">
<style>
  :root {
    --page: #ffffff;
    --kraft-light: #bb9a74;
    --kraft: #ae8b64;
    --kraft-dark: #9f7d58;
    --ink: #2c2216;
    --brand-ink: #4a4427;
    --band: #b8682c;
    --band-light: #c57a3c;
    --band-tab: #7a3f17;
    --variant-ink: #3a1d0a;
    --cream: #f6e6cc;
    --pill: #2a2723;
    --pill-text: #f2ede4;
    --berry: #b54a32;
    --leaf: #8a8a5a;
  }
  * { margin: 0; padding: 0; box-sizing: border-box; }
  html, body { width: 1200px; height: 955px; overflow: hidden; background: var(--page); }

  .canvas { position: relative; width: 1200px; height: 955px; }

  .label {
    position: absolute;
    left: 367px; top: 48px;
    width: 467px; height: 860px;
    background: linear-gradient(175deg, var(--kraft-light) 0%, var(--kraft) 55%, var(--kraft-dark) 100%);
    color: var(--ink);
    font-family: "Sorts Mill Goudy", Georgia, serif;
    overflow: hidden;
  }

  .brand {
    position: absolute;
    left: 0; right: 0; top: 120px;
    text-align: center;
    color: var(--brand-ink);
    font-family: "Sorts Mill Goudy", Georgia, serif;
    font-weight: 400;
  }
  .brand-name { display: block; font-size: 46px; line-height: 1.05; }
  .brand-tagline { display: block; font-size: 17px; letter-spacing: 2px; margin-top: 12px; text-transform: uppercase; }

  .product-type { position: absolute; left: 0; right: 0; text-align: center; }
  .product-type .kind { top: 0; }
  .product-line-1 { position: absolute; left: 0; right: 0; top: 336px; text-align: center; font-size: 22px; }
  .product-line-2 { position: absolute; left: 0; right: 0; top: 369px; text-align: center; font-size: 30px; }

  .scent-band {
    position: absolute;
    left: 0; right: 0; top: 427px; height: 133px;
    background: linear-gradient(180deg, var(--band-light), var(--band));
  }
  .band-tab { position: absolute; top: 57px; height: 30px; background: var(--band-tab); }
  .band-tab.left { left: 0; width: 97px; }
  .band-tab.right { right: 40px; width: 68px; }

  .scent-name {
    position: absolute; left: 0; right: 0; top: 12px;
    text-align: center;
    font-family: "Lobster Two", Georgia, cursive;
    font-style: italic; font-weight: 700;
    font-size: 30px;
    color: var(--variant-ink);
  }
  .scent-rule { position: absolute; left: 172px; top: 58px; }
  .scent-notes {
    position: absolute; left: 0; right: 0; top: 74px;
    text-align: center;
    font-size: 16.5px; line-height: 23px;
    color: var(--cream);
  }

  .botanical {
    position: absolute;
    left: 91px; top: 625px; width: 246px; height: 68px;
    background: radial-gradient(ellipse at 40% 60%, rgba(181,74,50,0.55), rgba(138,138,90,0.25) 55%, rgba(174,139,100,0) 80%);
    border-radius: 34px;
  }

  .benefit {
    position: absolute; left: 224px; top: 738px;
    font-family: "Libre Baskerville", Georgia, serif;
    font-weight: 700; font-size: 19px;
    color: var(--kraft-dark);
    text-shadow: -1px -1px 0 rgba(60,40,20,0.55), 1px 1px 0 rgba(255,240,220,0.35);
  }

  .volume {
    position: absolute; left: 179px; top: 784px;
    width: 68px; height: 27px;
    border-radius: 8px;
    background: var(--pill);
    color: var(--pill-text);
    font-size: 17px; line-height: 27px; text-align: center;
  }
</style>
</head>
<body>
<main class="canvas">
  <section class="label" aria-label="Organic hand wash label, Dunmoor scent">
    <div class="brand">
      <span class="brand-name">The Busy Wren</span>
      <span class="brand-tagline">Organic &amp; Natural Soaps</span>
    </div>

    <p class="product-line-1">Organic</p>
    <p class="product-line-2">Hand Washes</p>

    <div class="scent-band">
      <span class="band-tab left"></span>
      <span class="band-tab right"></span>
      <h1 class="scent-name">Dunmoor</h1>
      <svg class="scent-rule" width="123" height="6" viewBox="0 0 123 6" aria-hidden="true">
        <line x1="0" y1="3" x2="123" y2="3" stroke="#3a1d0a" stroke-width="1"/>
        <rect x="58" y="0.5" width="5" height="5" transform="rotate(45 60.5 3)" fill="#3a1d0a"/>
      </svg>
      <p class="scent-notes">sandalwood earthy tones with<br>a sandalwood powder exfoliant</p>
    </div>

    <div class="botanical" role="img" aria-label="Illustration of a sprig with red berries and slender green leaves"></div>

    <p class="benefit">Refreshing</p>
    <p class="volume">250 ml</p>
  </section>
</main>
</body>
</html>
```